KVR Biz Cards

We are a property management company that manages luxury level residential estates. As such, we need a business card design that gives a high end feel. The idea at the moment is to list the services offered on the back of the card, and our company information on the front of the card.

Services for the back of the card are as follows:
Professional Property Management service, Home Hosting & Concierge Service, Holliday Home / Income Property Management

```html
<!DOCTYPE html>
<html lang="en">
<head>
<meta charset="utf-8">
<title>KVR Biz Cards</title>
<link href="https://fonts.googleapis.com/css2?family=Arimo:ital,wght@0,400;0,700;1,400;1,700&family=Montserrat:wght@500;600;700&display=swap" rel="stylesheet">
<style>
  :root{
    --stage-top:#2e2e30;
    --stage-bottom:#4a4a4c;
    --card-black:#0d0d0d;
    --card-white:#ffffff;
    --gold:#8a5a24;
    --ink:#111111;
    --grey-text:#707070;
    --emboss:#3a3a3a;
  }
  *{box-sizing:border-box;margin:0;padding:0}
  html,body{width:1200px;height:976px;overflow:hidden}
  body{
    background:linear-gradient(160deg,var(--stage-top),var(--stage-bottom));
    font-family:"Arimo",Arial,sans-serif;
    position:relative;
  }
  .card{
    position:absolute;left:250px;width:700px;height:400px;
    box-shadow:0 14px 30px rgba(0,0,0,.45);
  }
  .card--back{top:58px;background:var(--card-black)}
  .card--front{top:518px;background:var(--card-white)}

  /* back */
  .services{position:absolute;left:56px;top:225px}
  .services__title{
    color:var(--gold);font-weight:700;font-style:italic;
    font-size:27px;letter-spacing:.5px;margin-bottom:14px;
  }
  .services__list{list-style:none}
  .services__item{
    color:#fff;font-style:italic;font-size:19px;line-height:28px;
    display:flex;align-items:center;gap:8px;
  }
  .tick{width:15px;height:15px;flex:none}
  .back-mark{
    position:absolute;right:60px;top:70px;
    font-family:"Montserrat",sans-serif;font-weight:600;
    font-size:110px;line-height:1;letter-spacing:6px;color:var(--emboss);
  }

  /* front */
  .brand{position:absolute;left:30px;top:110px;width:320px;text-align:center}
  .brand__mark{
    font-family:"Montserrat",sans-serif;font-weight:700;
    font-size:56px;letter-spacing:4px;color:var(--gold);line-height:1;
  }
  .brand__name{
    font-family:"Montserrat",sans-serif;font-weight:700;
    font-size:22px;color:var(--ink);margin-top:14px;letter-spacing:.5px;
  }
  .brand__tagline{
    font-family:"Montserrat",sans-serif;font-weight:500;
    font-size:14px;color:var(--gold);margin-top:4px;
  }
  .divider{position:absolute;left:360px;top:90px;width:1.5px;height:220px;background:var(--gold)}
  .contact{position:absolute;left:388px;top:92px;color:var(--grey-text);font-size:17px}
  .contact__name{color:var(--gold);font-weight:700;font-size:24px;letter-spacing:1px}
  .contact__role{font-size:17px;margin-bottom:18px}
  .contact__address{line-height:23px;margin-bottom:12px}
  .contact__line{display:flex;align-items:center;gap:7px;line-height:24px}
  .icon{width:13px;height:13px;flex:none;fill:var(--gold)}
</style>
</head>
<body>

<section class="card card--back" aria-label="Back of card">
  <div class="back-mark">KVR</div>
  <div class="services">
    <h2 class="services__title">SERVICES:</h2>
    <ul class="services__list">
      <li class="services__item"><svg class="tick" viewBox="0 0 16 16"><circle cx="8" cy="8" r="8" fill="var(--gold)"/><path d="M4.5 8.3l2.3 2.2 4.7-4.8" fill="none" stroke="#0d0d0d" stroke-width="1.8"/></svg>Professional Property Management service,</li>
      <li class="services__item"><svg class="tick" viewBox="0 0 16 16"><circle cx="8" cy="8" r="8" fill="var(--gold)"/><path d="M4.5 8.3l2.3 2.2 4.7-4.8" fill="none" stroke="#0d0d0d" stroke-width="1.8"/></svg>Home Hosting &amp; Concierge Service,</li>
      <li class="services__item"><svg class="tick" viewBox="0 0 16 16"><circle cx="8" cy="8" r="8" fill="var(--gold)"/><path d="M4.5 8.3l2.3 2.2 4.7-4.8" fill="none" stroke="#0d0d0d" stroke-width="1.8"/></svg>Holliday Home / Income Property Management</li>
    </ul>
  </div>
</section>

<section class="card card--front" aria-label="Front of card">
  <div class="brand">
    <div class="brand__mark">KVR</div>
    <div class="brand__name">KAVERLY RESIDENCE</div>
    <div class="brand__tagline">Curated Living, Effortless Comfort</div>
  </div>
  <div class="divider"></div>
  <div class="contact">
    <div class="contact__name">ADRIAN CALLOWAY</div>
    <div class="contact__role">President</div>
    <div class="contact__address">Harbour Court 4, Level 3<br>P.O. Box 12345, Marina Bay</div>
    <div class="contact__line"><svg class="icon" viewBox="0 0 16 16"><path d="M3.6 1l2.6 3.2-1.5 1.6c.9 2 2.4 3.6 4.5 4.6l1.6-1.5L14 11.5 12.6 14C6.7 13.6 2.3 9.2 2 3.3z"/></svg>000 555 0199</div>
    <div class="contact__line"><svg class="icon" viewBox="0 0 16 16"><path d="M1 3h14v10H1z M1 3l7 6 7-6" fill="none" stroke="var(--gold)" stroke-width="1.6"/></svg>info@kaverlyresidence.com</div>
    <div class="contact__line"><svg class="icon" viewBox="0 0 16 16"><g fill="none" stroke="var(--gold)" stroke-width="1.3"><circle cx="8" cy="8" r="6.5"/><ellipse cx="8" cy="8" rx="3" ry="6.5"/><path d="M1.5 8h13"/></g></svg>www.kaverlyresidence.com</div>
  </div>
</section>

</body>
</html>
```